New business card design needed for Trucking/Staffing company!

I am looking for a business card design. The business name is Keystone Haul Partners, LLC. This company is a staffing company for commercial drivers/truck drivers. Most of our customers are trucking/supply companies. Our colors are blue/black/white/grey. The info I have on my current business cards is
-Spot for a name
-2 lines for an address
-3 lines for Office, cell, and fax
-email
-website(currently on backside of card with logo but can go anywhere)
Updates

Project Deadline Extended
Reason: Open to more designs

Target Market(s)

Trucking companies, building supply companies

Industry/Entity Type

Business

Contact Information for Business Card

Edgy but professional

Font styles to use
Other font styles liked:
• Open to suggestions

Colors
0555a3
000000
ffffff
9d9d9d

Requirements
Must have
• Must have the logo incorporated

```html
<!DOCTYPE html>
<html lang="en">
<head>
<meta charset="utf-8">
<title>Keystone Haul Partners — Business Card</title>
<link rel="stylesheet" href="https://fonts.googleapis.com/css2?family=Open+Sans:wght@400;600;700;800&display=swap">
<style>
  :root {
    --brand-blue: #2c3d9e;
    --brand-blue-deep: #121f78;
    --brand-blue-light: #4656b4;
    --ink: #1c1c1c;
    --grey: #9d9d9d;
    --paper: #ffffff;
    --backdrop: #e9e9ec;
  }
  * { box-sizing: border-box; margin: 0; padding: 0; }
  html, body { width: 1200px; height: 913px; overflow: hidden; }
  body {
    background: var(--backdrop);
    font-family: "Open Sans", Arial, sans-serif;
    display: flex;
    align-items: center;
    justify-content: center;
    gap: 48px;
  }
  .card {
    position: relative;
    width: 540px;
    height: 309px;
    border-radius: 4px;
    box-shadow: 0 10px 28px rgba(0,0,0,.18);
    overflow: hidden;
  }
  .card--front { background: var(--paper); color: var(--brand-blue); }
  .card--back {
    background: linear-gradient(135deg, var(--brand-blue-light) 0%, var(--brand-blue) 45%, var(--brand-blue-deep) 100%);
    display: flex; align-items: center; justify-content: center;
  }

  .wordmark { display: flex; align-items: center; gap: 10px; font-weight: 800; letter-spacing: .5px; }
  .wordmark__mark { width: 16px; height: 16px; }
  .card--front .wordmark { position: absolute; left: 70px; top: 52px; color: var(--brand-blue-light); font-size: 22px; }
  .card--front .wordmark__mark { background: var(--brand-blue-light); }
  .card--back .wordmark { color: var(--paper); font-size: 30px; }
  .card--back .wordmark__mark { background: var(--paper); width: 20px; height: 20px; }

  .holder {
    position: absolute; right: 30px; top: 108px;
    font-size: 17px; font-weight: 700; letter-spacing: .3px;
    color: var(--brand-blue);
  }
  .holder__tab {
    position: absolute; right: 0; top: 104px;
    width: 0; height: 0;
    border-top: 26px solid var(--brand-blue-light);
    border-left: 14px solid transparent;
  }
  .rule { position: absolute; height: 1.5px; background: var(--brand-blue); }
  .rule--top { left: 190px; right: 18px; top: 134px; }
  .rule--bottom { left: 24px; width: 270px; top: 206px; }

  .address {
    position: absolute; right: 30px; top: 150px;
    text-align: right; font-size: 12.5px; line-height: 1.45;
    color: var(--brand-blue);
  }
  .contacts {
    position: absolute; left: 30px; top: 216px;
    list-style: none; font-size: 12.5px; line-height: 1.35;
    color: var(--brand-blue-deep);
  }
  .contacts li { display: flex; align-items: center; gap: 8px; }
  .contacts svg { width: 11px; height: 11px; flex: none; }
</style>
</head>
<body>
  <section class="card card--front" aria-label="Business card front">
    <div class="wordmark"><span class="wordmark__mark"></span>KEYSTONE HAUL PARTNERS</div>
    <span class="holder__tab"></span>
    <h1 class="holder">DALE MERCER</h1>
    <div class="rule rule--top"></div>
    <address class="address">48 Ridgeline Ave<br>Carlisle, PA 17013</address>
    <div class="rule rule--bottom"></div>
    <ul class="contacts">
      <li><svg viewBox="0 0 12 12"><path d="M3 1 L5 3.5 L4 5 Q5 7 7 8 L8.5 7 L11 9 L9.5 11 Q3 10 1 2.5 Z" fill="#222"/></svg>+33 2400-5180</li>
      <li><svg viewBox="0 0 12 12"><rect x="3" y="0.5" width="6" height="11" rx="1" fill="none" stroke="#222"/><circle cx="6" cy="9.5" r=".8" fill="#222"/></svg>+33 2400-5181</li>
      <li><svg viewBox="0 0 12 12"><rect x="3" y="1" width="6" height="3" fill="#222"/><rect x="1" y="4" width="10" height="5" rx="1" fill="#222"/><rect x="3" y="8" width="6" height="3" fill="#fff" stroke="#222"/></svg>+33-2400-5182</li>
      <li><svg viewBox="0 0 12 12"><rect x="1" y="2.5" width="10" height="7" fill="none" stroke="#222"/><path d="M1 2.5 L6 7 L11 2.5" fill="none" stroke="#222"/></svg>info@keystonehaul.com</li>
      <li><svg viewBox="0 0 12 12"><circle cx="6" cy="6" r="5" fill="none" stroke="#222"/><ellipse cx="6" cy="6" rx="2.2" ry="5" fill="none" stroke="#222"/><path d="M1 6 H11" stroke="#222"/></svg>www.keystonehaulpartners.com</li>
    </ul>
  </section>

  <section class="card card--back" aria-label="Business card back">
    <div class="wordmark"><span class="wordmark__mark"></span>KEYSTONE HAUL PARTNERS</div>
  </section>
</body>
</html>
```